Business Card & Letterhead Design

We a financial advice company based in Australia. We provide advice to wealthy farmers.

We are changing our business name FROM Brightmere Financial TO Calderstone Wealth and we need a new letterhead and double sided business card design

Attached is designs from our previous branding (Brightmere Financial) as it includes all the details we require on the new Calderstone Wealth business cards and letterhead.

```html
<!DOCTYPE html>
<html lang="en">
<head>
<meta charset="utf-8">
<title>Calderstone Wealth Stationery</title>
<link href="https://fonts.googleapis.com/css2?family=Open+Sans:wght@400;600;700&display=swap" rel="stylesheet">
<style>
:root{
  --bg:#c6c6c6;
  --charcoal:#524f4e;
  --slate:#6a6f74;
  --ink:#3a3a3a;
  --paper:#ffffff;
  --faint:#efefef;
  --window:#ececec;
}
*{margin:0;padding:0;box-sizing:border-box}
html,body{width:1200px;height:958px;overflow:hidden}
body{background:var(--bg);font-family:"Open Sans",Arial,sans-serif;color:var(--ink);position:relative}
.piece{position:absolute;background:var(--paper);box-shadow:6px 10px 16px rgba(0,0,0,.28);overflow:hidden}
.dark{background:var(--charcoal);color:#fff}
.ring{position:absolute;border:2px solid currentColor;border-radius:50%}
.brand-name{position:absolute;left:0;right:0;text-align:center;font-weight:400;letter-spacing:.04em;white-space:nowrap;text-transform:uppercase}
.brand-tag{position:absolute;left:0;right:0;text-align:center;letter-spacing:.26em;white-space:nowrap;text-transform:uppercase;opacity:.8}
.motto{position:absolute;left:0;right:0;text-align:center;font-size:6px;letter-spacing:.02em;text-transform:uppercase}

/* business card fronts */
.card{top:38px;width:211px;height:121px}
.card .ring{left:87px;top:31px;width:38px;height:38px}
.card .brand-name{top:68px;font-size:12.5px}
.card .brand-tag{top:84px;font-size:5px}
.card .motto{top:106px}
.card.light{color:var(--charcoal)}
.card .ghost{position:absolute;left:28px;top:-8px;width:150px;height:150px;border:3px solid rgba(255,255,255,.06);border-radius:50%}

/* card back */
.card-back{left:928px;color:var(--charcoal)}
.card-back .ring{left:51px;top:9px;width:24px;height:24px;border-width:1.5px}
.card-back .brand-name{left:8px;right:auto;width:110px;top:35px;font-size:7.6px;letter-spacing:.02em}
.card-back .brand-tag{left:8px;right:auto;width:110px;top:46px;font-size:3.3px;letter-spacing:.18em}
.person{position:absolute;right:12px;top:49px;text-align:right;font-size:4.3px;line-height:7px}
.person b{font-size:7px;font-weight:700}
.card-back hr{position:absolute;left:12px;right:12px;top:72px;border:0;border-top:.8px solid #888}
.contacts{position:absolute;left:12px;top:77px;font-size:4.5px;line-height:7.2px;list-style:none}
.contacts li{display:flex;align-items:center;gap:4px}
.contacts svg{width:5px;height:5px;fill:var(--charcoal)}
.card-back .addr{position:absolute;right:12px;top:77px;text-align:right;font-size:4.5px;line-height:7.2px}

.band{position:absolute;left:0;bottom:0;width:100%}
.band-url{position:absolute;right:12px;color:#fff;white-space:nowrap}

/* letterhead */
.letterhead{left:45px;top:196px;width:500px;height:707px;border-top:3px solid var(--charcoal);color:var(--charcoal)}
.letterhead .logo{position:absolute;left:30px;top:0;width:200px;height:110px}
.letterhead .ring{left:75px;top:28px;width:46px;height:46px}
.letterhead .brand-name{top:74px;font-size:17px}
.letterhead .brand-tag{top:94px;font-size:6.2px}
.sender{position:absolute;left:352px;top:26px;border-left:1px solid #777;padding-left:9px;height:126px;font-size:6.6px;line-height:9.3px;color:var(--ink);font-style:normal}
.sender h2{font-size:7.4px;font-weight:700;margin-bottom:5px;color:var(--charcoal);text-transform:uppercase}
.sender strong{font-weight:700;font-size:7.2px}
.sender p{margin-bottom:6px}
.sender .icon-row{display:flex;align-items:center;gap:6px}
.sender svg{width:6px;height:6px;fill:var(--charcoal)}
.body-copy{position:absolute;left:40px;top:205px;width:366px;font-size:7.7px;line-height:11.9px;letter-spacing:.02em;color:var(--ink)}
.body-copy p{margin-bottom:11.9px}
.signature{position:absolute;left:44px;top:432px;width:130px;height:18px;background:linear-gradient(90deg,#e4e4e4,#f4f4f4);border-radius:3px}
.watermark{position:absolute;border:6px solid var(--faint);border-radius:50%}
.letterhead .watermark{left:140px;top:418px;width:218px;height:218px}
.legal{position:absolute;top:656px;font-size:7px;line-height:8.6px;color:#222;white-space:nowrap}
.legal.sep{border-left:1px solid #777;height:16px;top:658px}

/* envelopes */
.env-back{left:616px;top:293px;width:523px;height:262px}
.flap{position:absolute;left:0;top:0}
.env-back .ring{left:242px;top:19px;width:40px;height:40px;color:#fff}
.env-back .brand-tag{top:60px;font-size:5px;color:#6b6867;opacity:1}
.return{position:absolute;left:0;right:0;top:236px;text-align:center;font-size:6.2px;color:#333}
.env-front{left:616px;top:643px;width:524px;height:262px;color:var(--charcoal)}
.env-front .ring{left:94px;top:28px;width:43px;height:43px}
.env-front .brand-name{left:15px;right:auto;width:200px;top:72px;font-size:15px}
.env-front .brand-tag{left:15px;right:auto;width:200px;top:90px;font-size:5.3px}
.env-front .address-window{position:absolute;left:35px;top:118px;width:208px;height:90px;background:var(--window);border:1px solid #d8d8d8;border-radius:4px}
.env-front .watermark{left:318px;top:33px;width:182px;height:182px}
</style>
</head>
<body>

<section class="piece card dark" style="left:47px">
  <span class="ring"></span>
  <div class="brand-name">Calderstone Wealth</div>
  <div class="brand-tag">Considered Rural Wealth Advice</div>
  <div class="motto">Clarity for the Long Season</div>
</section>

<section class="piece card light" style="left:341px">
  <span class="ring"></span>
  <div class="brand-name">Calderstone Wealth</div>
  <div class="brand-tag">Considered Rural Wealth Advice</div>
  <div class="motto">Clarity for the Long Season</div>
</section>

<section class="piece card dark" style="left:634px">
  <span class="ghost"></span>
  <span class="ring"></span>
  <div class="brand-name">Calderstone Wealth</div>
  <div class="brand-tag">Considered Rural Wealth Advice</div>
  <div class="motto">Clarity for the Long Season</div>
</section>

<section class="piece card card-back">
  <span class="ring"></span>
  <div class="brand-name">Calderstone Wealth</div>
  <div class="brand-tag">Considered Rural Wealth Advice</div>
  <div class="person"><b>Tom Reyner</b> B.Bus. Adv Dip FS<br>Managing Director<br>Authorised Representative</div>
  <hr>
  <ul class="contacts">
    <li><svg viewBox="0 0 10 10"><path d="M2 1l2 2-1 1.5c.6 1.2 1.3 1.9 2.5 2.5L7 6l2 2-1.5 1.5C4 9 1 6 .5 2.5z"/></svg>(07) 3155 2040</li>
    <li><svg viewBox="0 0 10 10"><rect x="2" y="0" width="6" height="3"/><rect x="0" y="3.5" width="10" height="4"/><rect x="2" y="7" width="6" height="3"/></svg>(07) 3155 2041</li>
    <li><svg viewBox="0 0 10 10"><rect x="3" y="0" width="4" height="10" rx="1"/></svg>0412 608 335</li>
    <li><svg viewBox="0 0 10 10"><path d="M0 2h10v6H0z"/></svg>info@calderstonewealth.com.au</li>
  </ul>
  <div class="addr">Suite 7C, 41 Arden St<br>Harwell Heights QLD 4572<br>PO Box 5183<br>Norbury QLD 4574</div>
  <svg class="band" viewBox="0 0 211 8" height="8" preserveAspectRatio="none">
    <rect x="0" y="2" width="211" height="6" fill="#6a6f74"/>
    <path d="M111 8 Q116 0 124 0 H211 V8Z" fill="#524f4e"/>
  </svg>
  <div class="band-url" style="bottom:1px;font-size:5px">www.calderstonewealth.com.au</div>
</section>

<section class="piece letterhead">
  <div class="logo">
    <span class="ring"></span>
    <div class="brand-name">Calderstone Wealth</div>
    <div class="brand-tag">Considered Rural Wealth Advice</div>
  </div>
  <address class="sender">
    <h2>Clarity for the Long Season</h2>
    <p><strong>Calderstone Wealth</strong><br>Corporate Authorised<br>Representative of Harbourline<br>Financial Planning Limited</p>
    <p>Suite 7C, 41 Arden St<br>Harwell Heights QLD 4572<br>PO Box 5183<br>Norbury QLD 4574</p>
    <div class="icon-row"><svg viewBox="0 0 10 10"><path d="M2 1l2 2-1 1.5c.6 1.2 1.3 1.9 2.5 2.5L7 6l2 2-1.5 1.5C4 9 1 6 .5 2.5z"/></svg>(07) 3155 2040</div>
    <div class="icon-row"><svg viewBox="0 0 10 10"><rect x="2" y="0" width="6" height="3"/><rect x="0" y="3.5" width="10" height="4"/><rect x="2" y="7" width="6" height="3"/></svg>(07) 3155 2041</div>
    <div class="icon-row"><svg viewBox="0 0 10 10"><path d="M0 2h10v6H0z"/></svg>info@calderstonewealth.com.au</div>
  </address>

  <div class="body-copy">
    <p>Lorem ipsum dolor sit amet, consectetur adipiscing elit. Praesent non est diam. Vivamus risus sem, gravida sit amet nibh ut, ornare lobortis ante. Aliquam sollicitudin, mauris tincidunt semper venenatis, orci est pretium augue, ut vestibulum felis velit bibendum urna. Integer sollicitudin aliquet ligula, non ultricies nisl efficitur nec. Aliquam felis lorem, facilisis ac condimentum quis, consectetur volutpat lacus. Proin fermentum sem quis elit efficitur, eu tempus magna maximus.</p>
    <p>Aenean a mi tortor. Morbi pretium mi sed cursus vehicula. Lorem ipsum dolor sit amet, consectetur adipiscing elit. In finibus eros ac maximus finibus. Nunc pretium pellentesque tellus. Nullam accumsan nisl non diam commodo sagittis. Nunc et ante sit amet urna auctor convallis. Maecenas sed fringilla metus, sit amet vulputate felis. Morbi eget tempor nisi. Aliquam erat volutpat. Aenean laoreet interdum tempus.</p>
    <p>Maecenas dignissim placerat mauris, vitae sollicitudin ex. Integer bibendum maximus mauris, ac tempor urna viverra id. Integer tincidunt lobortis nisl at posuere. Sed faucibus vulputate finibus. Maecenas convallis, sem quis pellentesque cursus, urna quam aliquam augue, quis porttitor eros est nec lectus. Sed mattis at tellus ut blandit. Aenean nunc magna, viverra sed mauris vel, porta finibus lacus. Nullam bibendum turpis rutrum porta placerat</p>
  </div>
  <div class="signature" role="img" aria-label="Handwritten signature of the sender"></div>
  <span class="watermark"></span>

  <div class="legal" style="left:40px">Harbourline Financial Planning Limited<br>ABN 41 118 520 637</div>
  <span class="legal sep" style="left:182px"></span>
  <div class="legal" style="left:196px">Australian Financial Services Licence<br>Licence Number 318 402</div>
  <span class="legal sep" style="left:340px"></span>
  <div class="legal" style="left:354px">Principle Address: 410 Tanner Lane<br>PO Box 4418 Elmsford VIC 3912</div>

  <svg class="band" viewBox="0 0 500 20" height="20" preserveAspectRatio="none">
    <rect x="0" y="10" width="500" height="10" fill="#6a6f74"/>
    <path d="M318 20 Q330 0 348 0 H500 V20Z" fill="#524f4e"/>
    <path d="M316 20 Q328 0 346 0" stroke="#fff" stroke-width="1.2" fill="none"/>
  </svg>
  <div class="band-url" style="bottom:5px;right:33px;font-size:7.5px">www.calderstonewealth.com.au</div>
</section>

<section class="piece env-back">
  <svg class="flap" width="523" height="78" viewBox="0 0 523 78">
    <path d="M0 0 H523 L505 62 Q500 78 484 78 H39 Q23 78 19 62 Z" fill="#524f4e"/>
  </svg>
  <span class="ring"></span>
  <div class="brand-tag">Considered Rural Wealth Advice</div>
  <div class="return">Calderstone Wealth • Suite 7C, 41 Arden St • Harwell Heights QLD 4572 • PO Box 5183 • Norbury QLD 4574</div>
</section>

<section class="piece env-front">
  <span class="watermark"></span>
  <span class="ring"></span>
  <div class="brand-name">Calderstone Wealth</div>
  <div class="brand-tag">Considered Rural Wealth Advice</div>
  <div class="address-window"></div>
  <svg class="band" viewBox="0 0 524 22" height="22" preserveAspectRatio="none">
    <rect x="0" y="12" width="524" height="10" fill="#6a6f74"/>
    <path d="M340 22 Q352 0 372 0 H524 V22Z" fill="#524f4e"/>
    <path d="M338 22 Q350 0 370 0" stroke="#fff" stroke-width="1.2" fill="none"/>
  </svg>
  <div class="band-url" style="bottom:6px;right:33px;font-size:7.5px">www.calderstonewealth.com.au</div>
</section>

</body>
</html>
```